Branding website for a Data Science company with 1 product

Branding website for a Data Science company, featuring our main product: Quorlink. The purpose of the website is to get potential clients to get a peek at what we do, but the main purpose is to get them to get in touch with us. The website will not answer all questions. Therefore the contact details and contact form is a must-have .

Target Market(s)

Potential new B2B clients with medium to large websites, application users (behind a login)

Industry/Entity Type

It Company

Coding

Coded - Design and coding required

Number of Pages Required

2 page

Font styles to use
Sans Serif

Colors

Designer to choose colors to be used in the design.

Requirements
Must have
• A contact form and branding a product

```html
<!DOCTYPE html>
<html lang="en">
<head>
<meta charset="utf-8">
<title>Orbitline Associates — Data Engineering &amp; Advisory</title>
<link href="https://fonts.googleapis.com/css2?family=Roboto:wght@300;400;500&family=Open+Sans:ital,wght@0,400;1,400&display=swap" rel="stylesheet">
<style>
:root{
  --orange:#e8461e;
  --ink:#333333;
  --muted:#555555;
  --grey-bg:#f3f3f3;
  --line:#bdbdbd;
  --dark:#2b2b2b;
  --white:#ffffff;
}
*{box-sizing:border-box;margin:0;padding:0}
html,body{width:1200px;height:3141px;overflow:hidden}
body{font-family:"Roboto",Arial,sans-serif;color:var(--ink);background:var(--white);position:relative}
section,header,footer{position:absolute;left:0;width:1200px}

/* Hero */
.hero{top:0;height:645px;background:linear-gradient(110deg,#1c2a3c 0%,#3d4c60 40%,#6a7280 65%,#3a3e46 100%)}
.hero-photo{position:absolute;inset:0}
.nav-bar{position:absolute;top:38px;left:0;width:1200px;height:60px}
.brand{position:absolute;left:126px;top:10px;display:flex;align-items:center;gap:10px;color:var(--white);font-weight:400;font-size:20px;letter-spacing:1px;white-space:nowrap}
.brand-dot{width:32px;height:32px;border-radius:50%;background:var(--white);flex:none}
.main-nav{position:absolute;left:482px;top:18px;display:flex;gap:34px}
.main-nav a{color:var(--white);text-decoration:none;font-size:17px;font-weight:400}
.hero-title{position:absolute;top:268px;width:100%;text-align:center;color:var(--white);font-weight:400;font-size:50px;letter-spacing:1px}
.hero-title .accent{background:var(--orange);padding:0 8px}
.hero-sub{position:absolute;top:340px;width:100%;text-align:center;color:var(--white);font-weight:400;font-size:34px;letter-spacing:1px}
.slider-dots{position:absolute;top:610px;left:557px;display:flex;gap:8px}
.slider-dots span{width:14px;height:14px;border-radius:50%;background:var(--white)}
.slider-dots span.active{background:transparent;border:2px solid var(--white)}

/* Headings */
.section-title{text-align:center;font-weight:400;font-size:28px;color:#444}
.mark{display:block;margin:0 auto;width:30px;height:30px;border-radius:50%;background:var(--orange)}

/* Who we are */
.who{top:645px;height:440px}
.who .mark{position:absolute;left:585px;top:62px}
.who .section-title{position:absolute;top:122px;width:100%}
.who-text{position:absolute;top:186px;left:196px;width:808px;text-align:center;font-family:"Open Sans",Arial,sans-serif;font-size:14.5px;line-height:22px;color:var(--muted)}
.who-text p+p{margin-top:12px}
.btn{display:block;background:var(--orange);color:var(--white);text-align:center;font-size:15px;text-decoration:none}
.who .btn{position:absolute;left:509px;top:352px;width:172px;height:38px;line-height:38px}

/* Services */
.services{top:1085px;height:544px;background:var(--grey-bg)}
.services .section-title{position:absolute;top:52px;width:100%}
.service-grid{position:absolute;left:117px;top:117px;width:1016px;height:358px;display:flex;box-shadow:0 0 4px rgba(0,0,0,.12)}
.service-card{position:relative;width:254px;height:358px;padding:0 44px}
.service-card.is-orange{background:var(--orange);color:var(--white)}
.service-card.is-light{background:linear-gradient(160deg,#ffffff 0%,#ececec 100%)}
.service-card.is-photo{background:linear-gradient(160deg,#8a8a8a 0%,#5e5e5e 100%);color:var(--white)}
.service-card.is-faded{background:linear-gradient(160deg,#f7f7f7 0%,#dcdcdc 100%)}
.service-icon{position:absolute;top:60px;left:44px;width:72px;height:72px}
.service-card h3{position:absolute;top:160px;left:44px;font-weight:400;font-size:23px;line-height:28px}
.service-card p{position:absolute;top:222px;left:44px;width:180px;font-family:"Open Sans",Arial,sans-serif;font-size:11.5px;line-height:15px;opacity:.85}
.service-card .more{position:absolute;top:296px;left:44px;font-size:13px;color:inherit;text-decoration:none;padding-bottom:5px;border-bottom:2px solid var(--orange)}
.service-card.is-orange .more{border-color:var(--white)}

/* Why we are */
.why{top:1629px;height:461px;background:linear-gradient(100deg,#3c4350 0%,#1d2a40 45%,#14284a 75%,#2c4a78 100%)}
.why .mark{position:absolute;left:585px;top:56px;background:var(--white)}
.why .section-title{position:absolute;top:120px;width:100%;color:var(--white)}
.why-text{position:absolute;top:172px;left:220px;width:760px;text-align:center;color:var(--white);font-family:"Open Sans",Arial,sans-serif;font-size:14px;line-height:21px}
.why-text p+p{margin-top:10px}

/* Testimonials */
.testimonials{top:2090px;height:461px}
.testimonials .section-title{position:absolute;top:50px;width:100%;color:var(--orange)}
.quote-card{position:absolute;left:253px;top:188px;width:708px;height:203px;border:2px solid var(--line);border-radius:102px}
.avatar{position:absolute;left:554px;top:121px;width:92px;height:92px;border-radius:50%;background:linear-gradient(150deg,#c9b8a6,#6d5a4c);border:3px solid var(--white)}
.quote{position:absolute;top:228px;left:340px;width:520px;text-align:center;font-family:"Open Sans",Arial,sans-serif;font-style:italic;font-size:15px;line-height:25px;color:#555}
.qmark{position:absolute;font-family:"Open Sans",Arial,sans-serif;font-size:60px;color:#aaa;font-style:italic;line-height:1}
.qmark.open{left:318px;top:210px}
.qmark.close{left:836px;top:282px}
.author{position:absolute;top:318px;width:100%;text-align:center;font-size:16px;color:#444}
.arrow{position:absolute;top:252px;width:24px;height:40px}
.arrow.prev{left:208px}.arrow.next{left:981px}

/* Contact */
.contact{top:2551px;height:439px;background:var(--orange)}
.contact .section-title{position:absolute;top:66px;width:100%;color:var(--white)}
.field{position:absolute;border:2px solid rgba(255,255,255,.9);color:var(--white);font-size:14px;padding:8px 10px}
.f-name{left:182px;top:138px;width:274px;height:40px}
.f-email{left:463px;top:138px;width:274px;height:40px}
.f-phone{left:745px;top:138px;width:275px;height:40px}
.f-message{left:182px;top:190px;width:838px;height:92px}
.submit{position:absolute;left:513px;top:307px;width:195px;height:48px;background:var(--dark);color:var(--white);font-size:18px;text-align:center;line-height:48px}

/* Footer */
.site-footer{top:2990px;height:151px}
.footer-nav{position:absolute;left:122px;top:48px;display:flex;gap:40px}
.footer-nav a{color:#222;text-decoration:none;font-size:16px}
.copyright{position:absolute;left:122px;top:82px;font-size:12px;color:#555}
.social{position:absolute;left:928px;top:39px;display:flex;gap:6px}
.social span{width:34px;height:34px;border-radius:50%;border:2px solid #222}
</style>
</head>
<body>

<header class="hero">
  <div class="hero-photo" role="img" aria-label="Photo of an engineer working at server racks in a data centre"></div>
  <div class="nav-bar">
    <div class="brand"><span class="brand-dot"></span>ORBITLINE ASSOCIATES</div>
    <nav class="main-nav">
      <a href="#who">WHO WEARE</a><a href="#services">SERVICES</a><a href="#why">WHY US</a><a href="#testimonials">TESTIMONIAL</a><a href="#contact">CONTACT</a>
    </nav>
  </div>
  <h1 class="hero-title">DATA <span class="accent">ENGINEERING</span> &amp; ADVISORY</h1>
  <p class="hero-sub">MORBI DIAM MAURIS VIVERRA</p>
  <div class="slider-dots"><span class="active"></span><span></span><span></span><span></span></div>
</header>

<section class="who" id="who">
  <span class="mark"></span>
  <h2 class="section-title">WHO WE ARE</h2>
  <div class="who-text">
    <p>We have a product called Quorlink. This is our on-demand, software-as-a-service to capture, learn and target our client’s website visitors and turn them into loyal customers.</p>
    <p>Because of the easy and quick setup clients can in a record time start targeting their visitors instead of doing a large investment in new technology and data science. We help our clients to identify their potential customers with the help of data science. We therefore consider ourselves a data science company.</p>
  </div>
  <a class="btn" href="#contact">LEARN MORE</a>
</section>

<section class="services" id="services">
  <h2 class="section-title">OUR SERVICES</h2>
  <div class="service-grid">
    <article class="service-card is-orange">
      <svg class="service-icon" viewBox="0 0 72 72" fill="none" stroke="#fff" stroke-width="2"><path d="M26 44c-6-4-9-10-9-16a19 19 0 0 1 38 0c0 6-3 12-9 16v6H26z"/><path d="M28 56h16M30 62h12"/></svg>
      <h3>Advisory<br>and Insights</h3>
      <p>ullamcorper est eget tempor cursus neque mi consectetuer mi a ultricies massa est</p>
      <a class="more" href="#contact">CLICK HERE</a>
    </article>
    <article class="service-card is-light" role="img" aria-label="Faded photo behind targeting service">
      <svg class="service-icon" viewBox="0 0 72 72" fill="none" stroke="#222" stroke-width="2.5"><circle cx="34" cy="38" r="26"/><circle cx="34" cy="38" r="16"/><circle cx="34" cy="38" r="5"/><path d="M34 38L58 14M52 12l6 2 2 6"/></svg>
      <h3>Targeting and<br>Optimization</h3>
      <p>ullamcorper est eget tempor cursus neque mi consectetuer mi a ultricies massa</p>
      <a class="more" href="#contact">CLICK HERE</a>
    </article>
    <article class="service-card is-photo" role="img" aria-label="Photo of server racks behind data engineering service">
      <svg class="service-icon" viewBox="0 0 72 72" fill="none" stroke="#fff" stroke-width="2"><circle cx="12" cy="14" r="5"/><circle cx="12" cy="36" r="5"/><circle cx="12" cy="58" r="5"/><circle cx="56" cy="24" r="5"/><circle cx="56" cy="50" r="5"/><path d="M17 14h16l18 10M17 36h16l18-12M17 36h16l18 14M17 58h16l18-8"/></svg>
      <h3>Data<br>Engineering</h3>
      <p>ullamcorper est eget tempor cursus neque mi consectetuer mi a ultricies massa</p>
      <a class="more" href="#contact">CLICK HERE</a>
    </article>
    <article class="service-card is-faded" role="img" aria-label="Faded photo of a person in a server room behind data privacy service">
      <svg class="service-icon" viewBox="0 0 72 72" fill="none" stroke="#222" stroke-width="2.5"><path d="M8 12h22l5 6h29v46H8z"/><rect x="36" y="40" width="20" height="16"/><path d="M40 40v-5a6 6 0 0 1 12 0v5"/></svg>
      <h3>Data Privacy<br>and Security</h3>
      <p>ullamcorper est eget tempor cursus neque mi consectetuer mi a ultricies massa est</p>
      <a class="more" href="#contact">CLICK HERE</a>
    </article>
  </div>
</section>

<section class="why" id="why" role="img" aria-label="Photo of a hand writing over a network map and globe">
  <span class="mark"></span>
  <h2 class="section-title">WHY WE ARE</h2>
  <div class="why-text">
    <p>Fusce ultricies orci ac feugiat suscipit leo massa sodales velit et scelerisque mi tortor at ipsum ligula augue bibendum accumsan vestibulum commodo a mi Morbi ornare gravida</p>
    <p>elit integer congue augue et malesuada iaculis ipsum dui aliquet felis at cursus magna nisl nec elit Praesent elementum elit at tellus nec ultricies sit amet porttitor mattis enim In massa libero interdum nec interdum vel blandit sed nulla in ullamcorper est eget tempor cursus neque mi consectetuer mi a ultricies massa est sed nisl Class aptent taciti sociosqu ad litora torquent per conubia nostra per inceptos</p>
  </div>
</section>

<section class="testimonials" id="testimonials">
  <h2 class="section-title">TESTIMONIALS</h2>
  <div class="quote-card"></div>
  <div class="avatar" role="img" aria-label="Portrait photo of the client"></div>
  <span class="qmark open">“</span>
  <p class="quote">Alamcorper est eget tempor cursus neque mi consectetuer mi a ultricies massa est sed nisl Class aptent taciti sociosqu ad litora torquent per conubia nostra per inceptos hymenaeos Proin nulla</p>
  <span class="qmark close">”</span>
  <p class="author">By Author Name</p>
  <svg class="arrow prev" viewBox="0 0 24 40"><path d="M20 4L6 20l14 16" fill="none" stroke="var(--orange)" stroke-width="5"/></svg>
  <svg class="arrow next" viewBox="0 0 24 40"><path d="M4 4l14 16L4 36" fill="none" stroke="var(--orange)" stroke-width="5"/></svg>
</section>

<section class="contact" id="contact">
  <h2 class="section-title">CONTACT FORM</h2>
  <div class="field f-name">Name</div>
  <div class="field f-email">Email address</div>
  <div class="field f-phone">Phone</div>
  <div class="field f-message">Message</div>
  <div class="submit">SUBMIT</div>
</section>

<footer class="site-footer">
  <nav class="footer-nav">
    <a href="#who">WHO WEARE</a><a href="#services">SERVICES</a><a href="#why">WHY US</a><a href="#testimonials">TESTIMONIAL</a><a href="#contact">CONTACT</a>
  </nav>
  <p class="copyright">© 2017 Company Name &nbsp;All right reserved &nbsp;Term of Use</p>
  <div class="social"><span></span><span></span><span></span><span></span></div>
</footer>

</body>
</html>
```